Club Lumora - Dermatology Consultation App

Club Lumora is launching a new Quince QWS App for online Dermatology consultation. We would appreciate a simple Scandinavian design which communicates trust, comfort and expensive feel. Most yacht designs have similar color palette, light wood colors and textures, but don’t be restricted by those in your artistic search.
The process is completed in three easy steps:
1. take a Snapshot.
2. Describe and Send it.
3. get Diagnosis and Treatment.
The Home screen should also have buttons - Start new Case, Follow up Visit, Rx Refill.
15% of the Home screen should also have a field/button - Medical Cosmetics Shop.
10% of the Home screen should also have a field or buttons for Our Partners (sponsors) – Talvine, Norelisa, Parlo, Ostra. (if you click you would be directed to their sites)
Note / Suggestion : Maybe you could use a larger picture of a dermatologist and have overlying fields and content, just for more influencing effect. (I am not a professional though)
Thank you so much.
Updates
Target Market(s)
24 - 59 Female
Industry/Entity Type
Club
Look and feel

```html
<!DOCTYPE html>
<html lang="en">
<head>
<meta charset="utf-8">
<title>Club Lumora – Visual Design, Mobile Application</title>
<link rel="stylesheet" href="https://fonts.googleapis.com/css2?family=Cormorant+Garamond:wght@500&family=Open+Sans:ital,wght@0,400;0,600;1,400&display=swap">
<style>
:root{
  --purple:#2e1466;
  --purple-deep:#24104f;
  --purple-band:#3a1b78;
  --gold:#c9a45c;
  --white:#ffffff;
  --ink:#3c2a6e;
  --text:#333333;
  --muted:#888888;
  --coral:#ee6f57;
  --pink:#d9559a;
  --violet:#5b3f9c;
  --teal:#3f8f7d;
  --yellow:#f2c02e;
  --green:#1f9a5a;
  --red:#e85a5a;
}
*{margin:0;padding:0;box-sizing:border-box}
html,body{width:1200px;height:2720px;overflow:hidden;background:var(--white)}
body{font-family:"Open Sans",Arial,sans-serif;color:var(--text)}
.board{position:absolute;left:0;top:0;width:1137px;height:2576px;transform:scale(1.0555);transform-origin:0 0}
.backdrop{position:absolute;left:0;top:0}
.brand{position:absolute;display:flex;align-items:center;gap:10px;font-family:"Cormorant Garamond",Georgia,serif;font-weight:500;color:var(--gold)}
.brand-hero{left:162px;top:128px;font-size:50px}
.brand-dot{width:70px;height:70px;border:2px solid var(--gold);border-radius:50%}
.headline{position:absolute;left:826px;top:136px;color:var(--white)}
.headline h1{font-weight:400;font-size:34px;line-height:38px;letter-spacing:.5px}
.headline p{font-size:19px;line-height:22px}
.step-label{position:absolute;font-size:19px;color:var(--ink);letter-spacing:.2px;line-height:24px}
.step-label .bar{position:absolute;width:7px;height:24px;top:0}
.screen{position:absolute;width:238px;height:423px;overflow:hidden;background:var(--purple);border-radius:4px;box-shadow:0 12px 40px rgba(30,10,70,.18)}
.status{position:absolute;top:0;left:0;right:0;height:20px;color:var(--white);font-size:10px;text-align:center;line-height:20px}
.status .sig{position:absolute;left:5px;top:6px;width:14px;height:6px;border-bottom:6px dotted var(--white)}
.status .bat{position:absolute;right:5px;top:6px;width:15px;height:7px;background:var(--white);border-radius:1px}
/* landing */
.landing .brand{left:56px;top:36px;font-size:20px;gap:6px}
.landing .brand-dot{width:26px;height:26px;border-width:1px}
.hero-photo{position:absolute;left:-30px;top:96px;width:145px;height:155px;border-radius:50%;border:2px solid var(--gold);background:radial-gradient(circle at 40% 50%,#4a3a7a,#22124a)}
.menu-arc{position:absolute;left:0;top:90px}
.menu-item{position:absolute;display:flex;align-items:center;gap:8px;color:var(--white);font-size:9px;font-weight:600}
.menu-item i{width:22px;height:22px;border-radius:50%;display:inline-block}
.shop{position:absolute;left:0;right:0;top:282px;height:50px;background:var(--purple-band);color:#d8d0ee;font-size:9px;font-style:italic;padding:17px 12px}
.shop svg{position:absolute;right:10px;top:20px}
.partners{position:absolute;left:0;right:0;top:332px;bottom:0;background:var(--white);padding:10px 11px}
.partners h3{font-size:7px;font-weight:600;color:#222;margin-bottom:6px}
.partner-grid{display:grid;grid-template-columns:1fr 1fr;row-gap:8px;font-size:15px;color:#333}
/* camera */
.cam-top{position:absolute;left:0;right:0;top:0;height:50px;background:var(--purple)}
.cam-photo{position:absolute;left:0;right:0;top:50px;height:258px;background:radial-gradient(ellipse at 70% 55%,#b45a6e 0%,#c99a88 35%,#d8b8a6 75%,#cfae9c 100%)}
.cam-tools{position:absolute;left:0;right:0;top:268px;height:40px;background:rgba(80,60,70,.35);color:var(--white);font-size:13px;padding:10px 14px}
.cam-base{position:absolute;left:0;right:0;top:308px;bottom:0;background:var(--white)}
.shutter{position:absolute;left:94px;top:35px;width:50px;height:50px;border-radius:50%;background:var(--red)}
/* describe */
.page-title{position:absolute;left:0;right:0;top:26px;text-align:center;color:var(--white);font-size:11px}
.back{position:absolute;left:12px;top:28px}
.intro{position:absolute;left:12px;right:14px;top:62px;color:var(--white);font-size:7.5px;line-height:13px}
.slot{position:absolute;width:42px;height:42px;border-radius:50%;border:1px dashed rgba(255,255,255,.45)}
.slot svg{position:absolute;left:15px;top:16px}
.slot-filled{border:none;background:radial-gradient(circle at 45% 45%,#b87a78,#9b6a5a)}
.slot-remove{position:absolute;right:-3px;top:-2px;width:11px;height:11px;border-radius:50%;background:var(--white)}
.form{position:absolute;left:0;right:0;top:265px;bottom:0;background:var(--white);padding:12px 11px}
.form label{font-size:8px;color:var(--muted)}
.form p{font-size:8px;line-height:13px;color:#333;margin-top:8px;padding-bottom:8px;border-bottom:1px solid #ddd}
.send{position:absolute;left:36px;top:110px;width:166px;height:29px;background:var(--green);color:var(--white);font-size:11px;text-align:center;line-height:29px;border-radius:2px}
/* plan */
.plan-title{position:absolute;left:0;right:0;top:24px;text-align:center;color:var(--white);font-size:11px;line-height:13px}
.plan-title small{display:block;font-size:7px;margin-top:4px;color:#d8d0ee}
.plan-card{position:absolute;left:12px;right:12px;top:82px;bottom:0;background:var(--white)}
.plan-head{display:flex;align-items:center;gap:8px;font-size:9px;font-weight:600;padding:6px 10px;border-bottom:1px solid #e6e6e6}
.plan-head i{width:16px;height:16px;border-radius:50%;background:var(--teal);display:inline-block}
.med{margin:0 8px 0 12px;padding:7px 0 5px;border-bottom:1px solid #eee}
.tag{display:inline-block;font-size:5px;padding:0 3px;border-radius:1px;line-height:7px}
.tag-cream{background:#ecd9b8;color:#6b5433}
.tag-tablet{background:var(--yellow);color:#5b4200}
.med h4{font-size:8px;font-weight:600;color:#222;margin-top:2px}
.med p{font-size:5.5px;line-height:8px;color:#555}
.dose{font-size:7px;font-weight:600;margin-top:3px}
.dose .a{color:#2b54c8}.dose .b{color:var(--coral)}
</style>
</head>
<body>
<div class="board">
  <svg class="backdrop" width="1137" height="2576" viewBox="0 0 1137 2576" aria-hidden="true">
    <defs>
      <linearGradient id="band" x1="0" y1="0" x2="1" y2="1">
        <stop offset="0" stop-color="#2b1261"/>
        <stop offset=".6" stop-color="#3a1a76"/>
        <stop offset="1" stop-color="#43207e"/>
      </linearGradient>
    </defs>
    <polygon points="0,0 1137,0 1137,395 0,733" fill="url(#band)" role="img" aria-label="Soft portrait backdrop in deep purple"/>
  </svg>

  <div class="brand brand-hero"><span class="brand-dot"></span>Club Lumora</div>
  <div class="headline"><h1>VISUAL DESIGN</h1><p>MOBILE APPLICATION</p></div>

  <!-- Landing -->
  <section class="screen landing" style="left:185px;top:380px">
    <div class="status"><span class="sig"></span>4:20 PM<span class="bat"></span></div>
    <div class="brand"><span class="brand-dot"></span>Club Lumora</div>
    <div class="hero-photo" role="img" aria-label="Dermatology clinic photo"></div>
    <svg class="menu-arc" width="160" height="180" viewBox="0 0 160 180" aria-hidden="true">
      <path d="M95 5 A120 120 0 0 1 95 170" fill="none" stroke="var(--gold)" stroke-width="2"/>
    </svg>
    <div class="menu-item" style="left:108px;top:102px"><i style="background:var(--yellow)"></i>New case</div>
    <div class="menu-item" style="left:131px;top:163px"><i style="background:var(--coral)"></i>Follow up visit</div>
    <div class="menu-item" style="left:107px;top:223px"><i style="background:var(--teal)"></i>RX refill</div>
    <div class="shop">Enter Medical Cosmetics Shop
      <svg width="12" height="10" viewBox="0 0 12 10"><path d="M1 5l3.5 3.5L11 1" fill="none" stroke="#3ecf7a" stroke-width="1.6"/></svg>
    </div>
    <div class="partners">
      <h3>OUR PARTNERS</h3>
      <div class="partner-grid"><span>Talvine</span><span>Norelisa</span><span>Parlo</span><span>Ostra</span></div>
    </div>
  </section>
  <div class="step-label" style="left:480px;top:694px"><span class="bar" style="left:-17px;background:var(--coral)"></span>LANDING SCREEN</div>

  <!-- Snapshot -->
  <section class="screen camera" style="left:728px;top:950px">
    <div class="cam-top">
      <svg style="position:absolute;left:16px;top:20px" width="12" height="12" viewBox="0 0 12 12"><path d="M1 1l10 10M11 1L1 11" stroke="#fff" stroke-width="1.8"/></svg>
      <svg style="position:absolute;right:14px;top:20px" width="16" height="12" viewBox="0 0 16 12"><path d="M1 6l4.5 4.5L15 1" fill="none" stroke="#fff" stroke-width="2"/></svg>
    </div>
    <div class="cam-photo" role="img" aria-label="Close-up photo of irritated skin"></div>
    <div class="cam-tools">
      <svg width="8" height="14" viewBox="0 0 8 14"><path d="M5 0L0 8h3l-1 6 6-9H5z" fill="#fff"/></svg> off
      <svg style="position:absolute;right:14px;top:12px" width="20" height="15" viewBox="0 0 20 15"><rect x="1" y="3" width="18" height="11" rx="2" fill="#fff"/><rect x="7" y="1" width="6" height="3" fill="#fff"/><circle cx="10" cy="8.5" r="3" fill="none" stroke="#6b5a66" stroke-width="1.3"/></svg>
    </div>
    <div class="cam-base">
      <div class="shutter">
        <svg style="position:absolute;left:15px;top:17px" width="20" height="16" viewBox="0 0 20 16"><rect x="1" y="3" width="18" height="12" rx="2" fill="#fff"/><rect x="7" y="1" width="6" height="3" fill="#fff"/><circle cx="10" cy="9" r="3.5" fill="var(--red)"/></svg>
      </div>
    </div>
  </section>
  <div class="step-label" style="left:503px;top:1121px">TAKE A SNAPSHOT<span class="bar" style="left:170px;background:var(--pink)"></span></div>

  <!-- Describe -->
  <section class="screen describe" style="left:160px;top:1417px">
    <div class="status"><span class="sig"></span>4:20 PM<span class="bat"></span></div>
    <svg class="back" width="8" height="12" viewBox="0 0 8 12"><path d="M7 1L2 6l5 5" fill="none" stroke="#fff" stroke-width="1.5"/></svg>
    <div class="page-title">Treatment</div>
    <p class="intro">This will help our dermatologists understand and evaluate your problems and formulate a prescriptions to suit your custom solutions</p>
    <div class="slot slot-filled" style="left:15px;top:124px" role="img" aria-label="Snapshot thumbnail"><span class="slot-remove"></span></div>
    <div class="slot" style="left:99px;top:124px"><svg width="11" height="9" viewBox="0 0 11 9"><rect y="2" width="11" height="7" rx="1" fill="#bbb"/><circle cx="5.5" cy="5.5" r="1.8" fill="var(--purple)"/></svg></div>
    <div class="slot" style="left:184px;top:124px"><svg width="11" height="9" viewBox="0 0 11 9"><rect y="2" width="11" height="7" rx="1" fill="#bbb"/><circle cx="5.5" cy="5.5" r="1.8" fill="var(--purple)"/></svg></div>
    <div class="slot" style="left:15px;top:193px"><svg width="11" height="9" viewBox="0 0 11 9"><rect y="2" width="11" height="7" rx="1" fill="#bbb"/><circle cx="5.5" cy="5.5" r="1.8" fill="var(--purple)"/></svg></div>
    <div class="slot" style="left:99px;top:193px"><svg width="11" height="9" viewBox="0 0 11 9"><rect y="2" width="11" height="7" rx="1" fill="#bbb"/><circle cx="5.5" cy="5.5" r="1.8" fill="var(--purple)"/></svg></div>
    <div class="slot" style="left:184px;top:193px"><svg width="11" height="9" viewBox="0 0 11 9"><rect y="2" width="11" height="7" rx="1" fill="#bbb"/><circle cx="5.5" cy="5.5" r="1.8" fill="var(--purple)"/></svg></div>
    <div class="form">
      <label>Describe</label>
      <p>Your skin has tiny holes called pores that that can become blocked by oil, bacteria, and dirt. When this occurs, you may develop a pimple or “zit.” If your skin is repeatedly affected by this condition</p>
      <div class="send">Send</div>
    </div>
  </section>
  <div class="step-label" style="left:482px;top:1690px"><span class="bar" style="left:-21px;background:var(--violet)"></span>DESCRIBE AND SEND IT.</div>

  <!-- Plan -->
  <section class="screen plan" style="left:684px;top:1943px">
    <div class="status"><span class="sig"></span>4:20 PM<span class="bat"></span></div>
    <svg class="back" width="8" height="12" viewBox="0 0 8 12"><path d="M7 1L2 6l5 5" fill="none" stroke="#fff" stroke-width="1.5"/></svg>
    <div class="plan-title">Maren’s<br>Treatment Plan<small>Created by Dr. Havel</small></div>
    <div class="plan-card">
      <div class="plan-head"><i></i>Treatment</div>
      <div class="med"><span class="tag tag-cream">Cream</span><h4>Tretinoin topical cream 0.025%</h4><p>Apply to the affected area to dry skin every other night<br>for the first two weeks. then every night as tolerated.</p></div>
      <div class="med"><span class="tag tag-tablet">Tablet</span><h4>Doxycycline Hyclate 100mg</h4><p>Take twice daily with small amount of tablet.</p><div class="dose"><span class="a">1</span> · <span class="b">0</span> · <span class="a">1</span></div></div>
      <div class="med"><span class="tag tag-cream">Cream</span><h4>Tretinoin topical cream 0.025%</h4><p>Apply to the affected area to dry skin every other night<br>for the first two weeks. then every night as tolerated.</p></div>
      <div class="med"><span class="tag tag-tablet">Tablet</span><h4>Doxycycline Hyclate 100mg</h4><p>Take twice daily with small amount of tablet.</p><div class="dose"><span class="a">1</span> · <span class="b">0</span> · <span class="a">1</span></div></div>
      <div class="med"><span class="tag tag-cream">Cream</span><h4>Tretinoin topical cream 0.025%</h4><p>Apply to the affected area to dry skin every other night<br>for the first two weeks. then every night as tolerated.</p></div>
    </div>
  </section>
  <div class="step-label" style="left:410px;top:2141px;text-align:right;width:181px">GET DIAGNOSIS AND TREATMENT<span class="bar" style="left:203px;height:48px;background:var(--teal)"></span></div>
</div>
</body>
</html>
```